I need a new business card design for my pharmacy.

I need a business card design. I will include my logo.
The card needs to be readable. I prefer to have my logo on one side along with my website, the other side includes the other information. Please use combination of black, neon green, white, and silver. This needs to catch the eye but yet be clearly visible and legible. Thanks

Industry/Entity Type

Pharmacy

Contact Information for Business Card

It needs to have the following information listed:
Mel's Apothecary Owner/Pharm D.
7134 North Brook Lane
Sioux Falls, SD 57231
Phone 605-318-6207
Fax 605-318-6209
email: mel@melsapothecary-example.com
www.melsapothecary-example.com
Store hours Monday-Friday 8 am- 7 pm
Saturday 8 am- 12 pm
Sunday Closed
Please utilize the colors black, white, and neon green, maybe silver.

Requirements
Must have
• It needs to be easily readable!
Nice to have
• It should catch the eye.
Should not have
• Do not use any other colors except listed: black, neon green, white, & silver.

```html
<!DOCTYPE html>
<html lang="en">
<head>
<meta charset="utf-8">
<title>Mel's Apothecary – Business Card</title>
<link href="https://fonts.googleapis.com/css2?family=Open+Sans:wght@400;600;700&display=swap" rel="stylesheet">
<style>
  :root {
    --ink: #1b1b1b;
    --green: #8dc63f;
    --white: #ffffff;
    --silver: #e4e4e4;
    --rule: #8a8a8a;
    --backdrop: #3a3a3a;
  }
  * { margin: 0; padding: 0; box-sizing: border-box; }
  html, body { width: 1200px; height: 834px; overflow: hidden; }
  body {
    background: var(--backdrop);
    font-family: "Open Sans", Arial, sans-serif;
    color: var(--ink);
    display: flex;
    align-items: center;
    justify-content: center;
    gap: 40px;
  }
  .card {
    position: relative;
    width: 540px;
    height: 309px;
    background: linear-gradient(135deg, var(--white) 0%, var(--silver) 100%);
    overflow: hidden;
  }
  .brand {
    display: flex;
    align-items: center;
    gap: 18px;
  }
  .brand-dot {
    width: 38px; height: 38px;
    border-radius: 50%;
    background: var(--green);
    flex: none;
  }
  .brand-divider {
    width: 1px; height: 64px;
    background: var(--rule);
    flex: none;
  }
  .brand-name {
    font-weight: 600;
    font-size: 34px;
    letter-spacing: -1px;
    color: var(--ink);
    white-space: nowrap;
  }

  /* Front */
  .card-front {
    display: flex;
    flex-direction: column;
    align-items: center;
    justify-content: center;
  }
  .hours-block { margin-top: 22px; text-align: center; font-size: 13px; line-height: 1.45; }
  .hours-title { color: var(--green); font-weight: 600; font-size: 14px; }
  .day { font-weight: 700; }
  .website {
    position: absolute;
    left: 0; right: 0; bottom: 18px;
    text-align: center;
    font-size: 12px;
    color: var(--ink);
    white-space: nowrap;
  }

  /* Back */
  .card-back .brand { position: absolute; top: 56px; left: 70px; }
  .card-back .brand-name { font-size: 36px; }
  .contact {
    position: absolute;
    right: 30px;
    top: 158px;
    width: 470px;
    text-align: right;
    font-size: 12px;
    white-space: nowrap;
  }
  .role { font-weight: 700; font-size: 15px; padding-right: 10px; }
  .role .title { color: var(--green); font-weight: 400; }
  .contact-rule { height: 1px; background: var(--rule); margin: 6px 0 7px 90px; }
  .address { margin-bottom: 6px; }
  .lines { display: flex; justify-content: flex-end; gap: 14px; font-size: 11.5px; }
  .lines span { display: inline-flex; align-items: center; gap: 5px; white-space: nowrap; flex: none; }
  .icon { width: 12px; height: 12px; flex: none; }
  .hours-band {
    position: absolute;
    left: 0; right: 0; bottom: 0;
    height: 30px;
    display: flex;
    font-size: 12px;
    white-space: nowrap;
  }
  .band-label {
    width: 100px;
    background: var(--ink);
    color: var(--green);
    font-weight: 600;
    display: flex; align-items: center; justify-content: center;
  }
  .band-hours {
    flex: 1;
    background: var(--green);
    color: var(--ink);
    display: flex; align-items: center;
    padding-left: 14px;
    gap: 4px;
  }
</style>
</head>
<body>

<section class="card card-front">
  <div class="brand">
    <div class="brand-dot"></div>
    <div class="brand-divider"></div>
    <div class="brand-name">Mel's Apothecary</div>
  </div>
  <div class="hours-block">
    <div class="hours-title">Store hours</div>
    <div><span class="day">Monday</span> Friday 8 am- 7 pm</div>
    <div><span class="day">Saturday</span> 8 am- 12 pm</div>
    <div><span class="day">Sunday</span> Closed</div>
  </div>
  <div class="website">www.melsapothecary-example.com</div>
</section>

<section class="card card-back">
  <div class="brand">
    <div class="brand-dot"></div>
    <div class="brand-divider"></div>
    <div class="brand-name">Mel's Apothecary</div>
  </div>
  <div class="contact">
    <div class="role">Pharm D. - <span class="title">Owner</span></div>
    <div class="contact-rule"></div>
    <div class="address">7134 North Brook Lane Sioux Falls, SD 57231</div>
    <div class="lines">
      <span><svg class="icon" viewBox="0 0 12 12"><path d="M1 4 Q6 0 11 4 L9.5 5.5 L8 4.5 L4 4.5 L2.5 5.5 Z M3 6 H9 L10 11 H2 Z" fill="var(--green)"/></svg>605-318-6207</span>
      <span><svg class="icon" viewBox="0 0 12 12"><rect x="3" y="1" width="6" height="4" fill="none" stroke="var(--green)"/><rect x="1" y="5" width="10" height="4" fill="var(--green)"/><rect x="3" y="8" width="6" height="3" fill="none" stroke="var(--green)"/></svg>605-318-6209</span>
      <span><svg class="icon" viewBox="0 0 12 12"><rect x="1" y="2.5" width="10" height="7" fill="none" stroke="var(--green)"/><path d="M1 2.5 L6 7 L11 2.5" fill="none" stroke="var(--green)"/></svg>mel@melsapothecary-example.com</span>
    </div>
  </div>
  <div class="hours-band">
    <div class="band-label">Store hours</div>
    <div class="band-hours">
      <span class="day">Monday</span> Friday 8 am- 7 pm
      <span class="day">&nbsp;Saturday</span> 8 am- 12 pm
      <span class="day">&nbsp;Sunday</span> Closed
    </div>
  </div>
</section>

</body>
</html>
```